Equipment Finance Specialist I work with companies who need the funds to buy their equipment

I would like a business card that stands out on the shelves. I want to be able to hand it to someone and say WOW. This card should have my logo.
You can put color into it I am very open on design and color

What my company does is we deal with dealerships that sell equipment such as Dump Trucks garbage trucks tractors trailers. Customers get referred to us and depending on their time in business we will ask for the following items

Companies that have been in business for more than two years we have a credit application program up to 250K . With this program we need the following items Credit application filled out(which is what I would like to be able for the customer to click on my website to get.) as well as three current month bank statements.

Deals over 250k we will need the following items

2 years business tax returns
2 years personal tax returns
Profit & Loss statement
Personal Financial Statement

what we do
100% FINANCING
SEASONAL PAYMENTS
LOAN BALLOON PAYMENTS
TRAC LEASING
LOW-INTEREST REFINANCING RATES
DEBT CONSOLIDATION

We specialize in creative financing solutions and offer a variety of reliable, flexible and expandable lending choices.

Target Market(s)

Trucking Companies

Industry/Entity Type

Trucking Company

Contact Information for Business Card

* $250,000 Application only Program
* Loans from $30,000 to 5,000,000
* Competitive Interest Rates

Font styles to use
Serif
Sans Serif

Colors

Designer to choose colors to be used in the design.

Requirements
Must have
• On the back of the card.
• * $250,000 Application only Program
• * Loans from $30,000 to 5,000,000
• My name, email, website. address
• * Competitive Interest Rates
• * 100% Financing
Nice to have
• I want my logo to pop on the card
• My logo is the great one I would like to use
Should not have
• I am up for your creativity as well

```html
<!DOCTYPE html>
<html lang="en">
<head>
<meta charset="utf-8">
<title>Crestline Financing – Business Card</title>
<link rel="stylesheet" href="https://fonts.googleapis.com/css2?family=Montserrat:wght@400;700;800&display=swap">
<style>
  :root {
    --bg: #2b2d30;
    --ink: #1b1b1c;
    --ink-soft: #6b6b6b;
    --paper: #ffffff;
    --dark-panel: #1f2022;
    --silver-light: #f2f2f2;
    --silver-mid: #a9abae;
    --silver-dark: #55575a;
  }
  * { box-sizing: border-box; margin: 0; padding: 0; }
  html, body {
    width: 1200px; height: 960px; overflow: hidden;
    background: var(--bg);
    font-family: "Montserrat", sans-serif;
  }
  .stage {
    position: relative; width: 1200px; height: 960px;
  }
  .card {
    position: absolute; left: 280px;
    width: 640px; height: 366px;
    border-radius: 26px; overflow: hidden;
    box-shadow: 0 18px 40px rgba(0,0,0,.45);
    background: var(--paper);
  }
  .card--front { top: 80px; }
  .card--back { top: 510px; }
  .card svg.card-art { position: absolute; inset: 0; width: 100%; height: 100%; }

  .brand {
    position: absolute; left: 110px; top: 36px;
    display: flex; align-items: center; gap: 18px;
    white-space: nowrap;
  }
  .brand-dot {
    width: 74px; height: 74px; border-radius: 50%; flex: none;
    background: var(--silver-mid);
  }
  .brand-name {
    color: var(--silver-light);
    font-weight: 800; font-size: 36px; line-height: 1.0;
    letter-spacing: 2px; text-transform: uppercase;
  }
  .equipment-art {
    position: absolute; right: 40px; top: 60px;
    width: 78px; height: 150px; border-radius: 6px;
    background: linear-gradient(160deg, #d9d9d9, #7b7d80);
    opacity: .85;
  }
  .website {
    position: absolute; left: 70px; bottom: 70px;
    color: var(--ink); font-weight: 800; font-size: 24px;
  }

  .offer-list {
    position: absolute; left: 60px; right: 60px; top: 50%;
    transform: translateY(-50%);
    list-style: none; text-align: center;
    color: var(--ink-soft); font-size: 25px; line-height: 1.38;
  }
  .offer-list strong { color: var(--ink); font-weight: 700; }
</style>
</head>
<body>
<main class="stage">

  <section class="card card--front" aria-label="Card front">
    <svg class="card-art" viewBox="0 0 640 366" preserveAspectRatio="none" aria-hidden="true">
      <defs>
        <linearGradient id="silverSweep" x1="0" y1="0" x2="1" y2="0">
          <stop offset="0" stop-color="#5a5c5f"/>
          <stop offset=".45" stop-color="#f4f4f4"/>
          <stop offset=".7" stop-color="#8d8f92"/>
          <stop offset="1" stop-color="#e6e6e6"/>
        </linearGradient>
      </defs>
      <path d="M0 0 H640 V366 H600 C470 250 260 150 0 150 Z" fill="url(#silverSweep)"/>
      <path d="M0 0 H640 V366 H618 C490 236 270 136 0 134 Z" fill="var(--dark-panel)"/>
    </svg>
    <div class="brand">
      <span class="brand-dot"></span>
      <span class="brand-name">Crestline<br>Financing</span>
    </div>
    <div class="equipment-art" role="img" aria-label="Silver crane boom illustration"></div>
    <p class="website">www.yourwebsite.com</p>
  </section>

  <section class="card card--back" aria-label="Card back">
    <svg class="card-art" viewBox="0 0 640 366" preserveAspectRatio="none" aria-hidden="true">
      <defs>
        <linearGradient id="edgeBand" x1="0" y1="0" x2="0" y2="1">
          <stop offset="0" stop-color="#6a6c6f"/>
          <stop offset=".35" stop-color="#f2f2f2"/>
          <stop offset=".6" stop-color="#9a9c9f"/>
          <stop offset="1" stop-color="#3f4143"/>
        </linearGradient>
      </defs>
      <rect x="0" y="0" width="44" height="366" fill="url(#edgeBand)"/>
      <rect x="596" y="0" width="44" height="366" fill="url(#edgeBand)"/>
    </svg>
    <ul class="offer-list">
      <li><strong>$250,000</strong> Application only Program</li>
      <li>Loans from <strong>$30,000 to 5,000,000</strong></li>
      <li>Competitive Interest Rates</li>
      <li><strong>100%</strong> Financing</li>
    </ul>
  </section>

</main>
</body>
</html>
```